A 'new law' boutique Australian law firm that provides specialist employment law and people managem

We value helping clients create results with respect workplaces. What differentiates us is we provide actionable training in understanding and dealing with people and ensure legal compliance fits with this approach. We would like a fresh approach to our training overview documents that we currently use in our current law firm (6 attached). Please use pictures, symbols etc consistent with our non-traditional law approach that captures the approach of each training session.. Attached is the logo and draft letterhead for Brook Legal which will launch soon.

Target Market(s)

HR Managers and in-house lawyers (non employment specialists) in mid-large Australian companies that are progressive with a relationship based approach to managing employee behaviours and disputes.

Industry/Entity Type

Human Resource

Font styles to use
Sans Serif

Colors
3176b5
33a6d7

Requirements
Must have
• 1 or 2 page PDF for each of the 6 documents that the wording supplied goes into your design which will be pretty similar as we want consistency with our documents

```html
<!DOCTYPE html>
<html lang="en">
<head>
<meta charset="utf-8">
<title>Contact Officer Training – Brook Legal</title>
<link href="https://fonts.googleapis.com/css2?family=Merriweather:wght@400;700&display=swap" rel="stylesheet">
<style>
  :root{
    --brand-blue:#3176b5;
    --sky:#33a6d7;
    --sky-mid:#7cc8ea;
    --sky-pale:#cfeefa;
    --charcoal:#2b2b2d;
    --ink:#1f3550;
    --paper:#ffffff;
    --backdrop:#3a3a3c;
  }
  *{box-sizing:border-box;margin:0;padding:0}
  html,body{width:1200px;height:800px;overflow:hidden}
  body{background:var(--backdrop);font-family:"Merriweather",serif;color:var(--ink)}
  .flyer{position:absolute;left:317px;top:0;width:566px;height:800px;background:var(--paper);overflow:hidden}

  /* left column */
  .masthead{position:absolute;left:0;top:0;width:336px;height:62px}
  .masthead-band{position:absolute;left:0;top:0;width:336px;height:62px}
  .brand{position:absolute;left:20px;top:22px;font-weight:400;font-size:15px;color:var(--ink)}
  .contact{position:absolute;right:14px;top:14px;font-size:7px;color:#fff;line-height:1.9}
  .contact span{display:flex;align-items:center;gap:4px}
  .contact svg{width:8px;height:8px}

  .need-panel{position:absolute;left:0;top:62px;width:336px;height:430px;background:var(--charcoal);
    clip-path:polygon(0 0,300px 0,336px 30px,336px 100%,40px 100%,0 91%)}
  .title{position:absolute;right:26px;top:42px;text-align:right;line-height:1.15}
  .title .lead{display:block;color:#fff;font-size:20px;font-weight:700}
  .title .main{display:block;color:var(--sky);font-size:22px;font-weight:700}
  .need-heading{position:absolute;right:26px;top:112px;color:var(--sky);font-size:11px;font-weight:700}
  .need-text{position:absolute;right:26px;top:134px;width:255px;text-align:right;color:#e9e9e9;font-size:7px;line-height:1.65}
  .need-text p{margin-bottom:10px}

  .icon-badge{position:absolute;left:130px;top:455px;width:74px;height:74px;border-radius:50%;background:#fff;display:flex;align-items:center;justify-content:center}
  .icon-fill{width:60px;height:60px;border-radius:50%;background:linear-gradient(160deg,var(--sky),var(--brand-blue))}

  .outcomes{position:absolute;left:22px;top:548px;width:300px}
  .outcomes h2{color:var(--sky);font-size:13px;font-weight:700;margin-bottom:8px}
  .outcomes .intro{font-size:7.5px;font-weight:700;line-height:1.5;margin-bottom:6px}
  .outcomes ol{font-size:7.5px;line-height:1.7;padding-left:12px}

  /* right column */
  .overview{position:absolute;left:336px;top:0;width:230px;height:800px;display:flex;flex-direction:column}
  .topic{padding:8px 14px 8px 16px;font-size:6.6px;line-height:1.45;flex:auto}
  .topic h3{font-size:9px;font-weight:700;margin-bottom:3px;color:var(--ink)}
  .topic .q{font-weight:700}
  .topic ul{padding-left:9px}
  .t-deep{background:var(--sky)}
  .t-mid{background:var(--sky-mid)}
  .t-pale{background:var(--sky-pale)}
  .t-head{background:var(--brand-blue);color:#fff;flex:0 0 auto;padding-top:14px}
  .t-head h2{font-size:12px;color:#fff}
</style>
</head>
<body>
<main class="flyer">
  <header class="masthead">
    <svg class="masthead-band" viewBox="0 0 336 62" aria-hidden="true"><polygon points="170,0 336,0 336,62 205,62" fill="var(--brand-blue)"/></svg>
    <div class="brand">Brook Legal</div>
    <div class="contact">
      <span><svg viewBox="0 0 10 10"><circle cx="5" cy="5" r="4.5" fill="none" stroke="#fff"/><path d="M.5 5h9M5 .5v9" stroke="#fff"/></svg>www.brooklegal.com.au</span>
      <span><svg viewBox="0 0 10 10"><rect x=".5" y="2" width="9" height="6" fill="none" stroke="#fff"/><path d="M.5 2l4.5 3.5L9.5 2" fill="none" stroke="#fff"/></svg>info@brooklegal.com.au</span>
    </div>
  </header>

  <section class="need-panel">
    <h1 class="title"><span class="lead">Contact</span><span class="main">Officer Training</span></h1>
    <h2 class="need-heading">Training Need</h2>
    <div class="need-text">
      <p>Unlawful or inappropriate behaviour in the workplace that is left unaddressed can impact on productivity and employee retention. Claims can be costly in terms of time and money as well as the impact on mental health from being involved in uncomfortable adversarial processes.</p>
      <p>Clear policies and procedures explaining the organisation's workplace behaviour expectations and how grievances will be managed are a minimum compliance requirement.</p>
      <p>The challenge is ensuring that employees understand the directions contained in those policies, what is unlawful and inappropriate behaviour and the options available to address those behaviours if they experience them or engage in them.</p>
      <p>Well trained Contact Officers provide another resource to assist the organisation to provide a safe and respectful workplace.</p>
    </div>
  </section>

  <div class="icon-badge"><div class="icon-fill" role="img" aria-label="Icon of a presenter at a board with a seated group"></div></div>

  <section class="outcomes">
    <h2>Learning Outcomes</h2>
    <p class="intro">Training will enable participants to perform their role of Contact Officer and to understand:</p>
    <ol>
      <li>The role and responsibilities of a Contact Officer.</li>
      <li>What amounts to unlawful workplace behaviour.</li>
      <li>What is considered inappropriate behaviour in our workplace.</li>
      <li>How to apply understanding unlawful/inappropriate behaviour to common scenarios.</li>
      <li>How to address and resolve grievances early.</li>
      <li>Options to resolve grievances internally and the Contact Officer role.</li>
      <li>External options and their pros and cons for resolving grievances.</li>
    </ol>
  </section>

  <aside class="overview">
    <div class="topic t-head"><h2>Training Overview</h2></div>
    <div class="topic t-deep">
      <h3>Discrimination</h3>
      <p class="q">What is direct and indirect discrimination?</p>
      <ul><li>What are the prescribed attributes?</li><li>What are the exceptions to the general rules?</li></ul>
      <p class="q">Practical examples of behaviour that may be discriminatory.</p>
    </div>
    <div class="topic t-mid">
      <h3>Harassment</h3>
      <p class="q">What is harassment?</p>
      <ul><li>Are protected attributes relevant to harassment?</li><li>What is the difference between harassment and sexual harassment?</li><li>How does the reasonable person test work in relation to harassment?</li></ul>
      <p class="q">Practical examples of behaviour that may be harassment or sexual harassment.</p>
    </div>
    <div class="topic t-pale">
      <h3>Bullying</h3>
      <p class="q">What is bullying?</p>
      <ul><li>Explain how bullying differs to discrimination or inappropriate behaviour.</li><li>Performance Management – when it will and will not be bullying.</li><li>Is all workplace conflict bullying?</li></ul>
      <p class="q">Practical examples of behaviour that may be bullying.</p>
    </div>
    <div class="topic t-deep">
      <h3>Victimisation &amp; Vilification</h3>
      <p class="q">What is Victimisation? What is Vilification?</p>
    </div>
    <div class="topic t-mid">
      <h3>Adverse Action</h3>
      <p class="q">What is adverse action and how does it differ to other unlawful behaviour?</p>
      <ul><li>What is a workplace right?</li><li>When is it lawful to terminate employment because of an employee's absence?</li><li>How are the protected attributes relevant to adverse action?</li></ul>
    </div>
    <div class="topic t-pale">
      <h3>The Contact Officer's role</h3>
      <ul><li>How to perform your role when approached by an employee – the 6 step approach. What not to do.</li><li>What are the obligations with regard to Confidentiality?</li></ul>
    </div>
    <div class="topic t-deep">
      <h3>Grievance Options</h3>
      <ul><li>Explain the options of complaint management – self management, internal informal management, formal internal management.</li><li>How do they compare and what are the advantages and disadvantages of each approach. Is doing nothing an option?</li><li>External options – advantages and disadvantages. Who decides which option?</li></ul>
    </div>
    <div class="topic t-mid">
      <h3>Test Learning</h3>
      <ul><li>Role plays, group discussion.</li></ul>
    </div>
  </aside>
</main>
</body>
</html>
```